Web Design Project

Dear designer(s),

I need a design for a shop who's specialized into...

-Material to fix or do tailor made clothing (cloth, buttons, zippers etc)
-Curtains (static/pull-up)
-Blinds (plastic/wood)

that kind of stuff.

Good thing is that I can provide a lot of pretty photo's to work with. I have 3.5 Gigabyte of 300-1200 dpi photo's altho I converted most of them to 72dpi for your convenience (75Mb).

You can download the working material from this quillbarn link:

http://files.quillbarn.net/u/31862094/Velunor.zip

this is an updated file, it contains the dutch menu items to use in your design

http://files.quillbarn.net/u/31862094/Velunor_Content.txt

Notice: take your time to come up with something nice. I prefer 1 or 2 designs from a designer that has been thinked of, than 5 quick ones.
Updates

Thank you for those who posted designs already but I want to clarify something.

As I mentioned it's a shop, that's a physical shop and not a webshop.

So you can safe some time and skip drawing the shopping cart icons, shop items on the homepage and other shop related things.

They don't want to start online reselling as they already spend most of their time in their shop to catch up with all orders.

Keep up the good work!

Industry/Entity Type

Clothing

Requirements
Nice to have
• Maybe the hi-res pictures can be used as background ratotor that appears left/right next to the centered website content?

Since there is a lot of material each section might have his topic linked set of thumbnails that opens a bigger image on clicking?

```html
<!DOCTYPE html>
<html lang="nl">
<head>
<meta charset="utf-8">
<title>Velunor</title>
<link href="https://fonts.googleapis.com/css2?family=Open+Sans:wght@400;600;700&family=Arimo:wght@400;700&display=swap" rel="stylesheet">
<style>
:root{
  --blue:#0a74c4;
  --blue-dark:#0560a8;
  --ink:#222;
  --grey:#555;
  --line:#dcdcdc;
  --panel:#f4f4f5;
  --dark:#2a2a2a;
  --icon:#9a9a9a;
}
*{margin:0;padding:0;box-sizing:border-box}
html,body{width:953px;height:1200px;overflow:hidden;background:#fff}
body{position:relative;font-family:Arimo,Arial,sans-serif;color:var(--ink)}
.abs{position:absolute}
.top-rule{left:0;top:0;width:953px;height:3px;background:var(--blue)}
.header-bg{left:0;top:3px;width:953px;height:80px;background:linear-gradient(#ededee,#fff)}
.logo{left:102px;top:24px;font-family:"Open Sans",sans-serif;font-weight:700;font-size:36px;color:var(--blue);letter-spacing:-1px}
.logo-dot{left:243px;top:28px;width:10px;height:10px;border-radius:50%;background:var(--blue)}
.nav{left:319px;top:35px;width:553px;height:29px;background:var(--blue);border-radius:4px;display:flex;align-items:center;padding:0 4px;justify-content:space-between}
.nav a{color:#fff;font-weight:700;font-size:10px;text-decoration:none;padding:4px 5px;border-radius:3px}
.nav a.active{background:#fff;color:var(--blue)}
.slider{left:81px;top:107px;width:791px;height:345px;border:1px solid var(--line);background:#fff}
.slide{left:90px;top:115px;width:774px;height:327px;background:linear-gradient(#9aa3ab 0%,#c7cbce 40%,#8d8c89 70%,#a9a6a1 100%)}
.slide-title{left:112px;top:174px;font-family:"Open Sans",sans-serif;font-weight:700;font-size:39px;line-height:39px;color:var(--blue);letter-spacing:-0.5px;text-shadow:0 0 2px #fff,0 0 2px #fff,2px 3px 4px rgba(0,0,0,.45)}
.arrow{top:250px;width:38px;height:38px}
.dots{left:404px;top:418px;width:127px;height:24px;background:#fff;border-radius:6px 6px 0 0;display:flex;justify-content:center;align-items:center;gap:5px}
.dots i{width:15px;height:15px;border-radius:50%;background:var(--blue);display:block}
.dots i.on{background:#bbb}
.slide-shadow{left:20px;top:448px;width:913px;height:40px;background:radial-gradient(ellipse at center top,rgba(0,0,0,.45),rgba(0,0,0,0) 70%)}
.welcome{left:99px;top:505px;width:771px;height:261px;border:1px solid var(--line);background:var(--panel)}
.welcome-head{left:99px;top:505px;width:771px;height:31px;background:linear-gradient(#fff,#ebebec);border:1px solid var(--line);font-size:17.5px;color:var(--blue);padding:6px 11px}
.welcome-img{left:110px;top:550px;width:208px;height:206px;background:linear-gradient(#e4e0e6,#b8c2c4 60%,#a7b1b3)}
.welcome-text{left:331px;top:551px;width:522px;font-size:10.4px;line-height:14.4px;text-align:justify;color:#1c1c1c;letter-spacing:.15px}
.welcome-text p+p{margin-top:14px}
.btn-dark{left:789px;top:730px;width:61px;height:21px;background:#222;color:#fff;font-size:10px;border-radius:3px;display:flex;align-items:center;justify-content:center}
.thumbs{left:99px;top:786px;width:757px;height:104px;border:1px solid #e2e2e2;background:#fff;box-shadow:inset 0 0 12px rgba(0,0,0,.08)}
.thumb{top:802px;width:102px;height:70px;border:2px solid #ccc}
.t1{left:154px;background:linear-gradient(90deg,#8a8a88,#bcbcbc)}
.t2{left:286px;background:linear-gradient(#b5bcc2,#d9d9d7)}
.t3{left:426px;background:linear-gradient(90deg,#b36a3a,#7a4a7a,#a7b9c4)}
.t4{left:565px;background:linear-gradient(90deg,#d9dde0,#c79a5a)}
.t5{left:697px;background:linear-gradient(90deg,#b09090,#8a98b0,#9a9a9a)}
.mini{top:829px;width:18px;height:18px}
.lower{left:0;top:920px;width:953px;height:213px;background:linear-gradient(#f0f0f1,#fafafa)}
.col-title{top:936px;font-family:"Open Sans",sans-serif;font-weight:600;font-size:14.5px;color:var(--blue)}
.col-icon{top:932px}
.col-rule{top:962px;height:1px;background:var(--line)}
.news-item{left:123px;width:215px;font-size:10px;line-height:14px;color:var(--grey)}
.posted{left:123px;font-size:8.5px;color:#333}
.news-arrow{left:103px;font-size:10px;color:#777}
.view-all{left:99px;top:1086px;width:238px;height:23px;background:linear-gradient(90deg,#d5dde6,#eef1f4,#d5dde6);font-size:9.5px;color:#333;display:flex;align-items:center;justify-content:center}
.video{left:359px;top:981px;width:238px;height:127px;border:4px solid #ccc;background:linear-gradient(90deg,#3a3a3a,#7a7e84 40%,#aaa 60%,#b0312a)}
.input{left:622px;width:228px;height:30px;background:#fff;border:1px solid #c9c9c9;border-radius:3px;font-size:9.5px;font-style:italic;color:#777;padding:9px 11px}
.submit{left:780px;top:1064px;width:71px;height:26px;border-radius:13px;background:linear-gradient(#555,#111);color:#fff;font-weight:700;font-size:10.5px;display:flex;align-items:center;justify-content:center}
.footer{left:0;top:1133px;width:953px;height:62px;background:var(--dark)}
.footer-links{left:93px;top:1147px;font-size:10px;color:#fff;word-spacing:1px}
.copyright{left:93px;top:1166px;font-size:8.5px;color:#fff}
.bottom-rule{left:0;top:1195px;width:953px;height:5px;background:var(--blue)}
</style>
</head>
<body>
<div class="abs top-rule"></div>
<div class="abs header-bg"></div>
<div class="abs logo">velunor</div>
<div class="abs logo-dot"></div>
<nav class="abs nav">
  <a class="active">Fashion fabrics</a><a>Table linen</a><a>Decorative fabrics</a><a>Retrieval Systems</a><a>Scholarships</a><a>Contact</a><a>Stock sale</a>
</nav>

<div class="abs slide-shadow"></div>
<svg class="abs arrow" style="left:67px" viewBox="0 0 38 38"><circle cx="19" cy="19" r="17" fill="#fff" stroke="#555" stroke-width="3"/><path d="M8 19 L17 13 L17 25Z" fill="#333"/></svg>
<svg class="abs arrow" style="left:848px" viewBox="0 0 38 38"><circle cx="19" cy="19" r="17" fill="#fff" stroke="#555" stroke-width="3"/><path d="M30 19 L21 13 L21 25Z" fill="#333"/></svg>
<div class="abs slider"></div>
<div class="abs slide" role="img" aria-label="White linen cloth draped over driftwood on a pebble beach with jugs and bottles"></div>
<div class="abs slide-title">Exclusief aanbod aan bruids<br>en feest stoffen.</div>
<div class="abs dots"><i></i><i class="on"></i><i></i><i></i><i></i></div>

<div class="abs welcome"></div>
<div class="abs welcome-head">Welcome to velunor</div>
<div class="abs welcome-img" role="img" aria-label="Table covered with a striped grey tablecloth, plates and a flower vase"></div>
<div class="abs welcome-text">
  <p>Lorem Ipsum is simply dummy text of the printing and typesetting industry. Lorem Ipsum has been the industry's standard dummy text ever since the 1500s, when an unknown printer took a galley of type and scrambled it to make a type specimen typesetting industry. Lorem Ipsum has been the industry's standard dummy text ever since the 1500s, when an unknown printer took a galley of type and scrambled it to make a type specimenbook. It has survived not only five centuries,</p>
  <p>But also Ipsum has been the industry's standard dummy text ever since the took a galley of type and scrambled it to make a type specimen book. It has survived typesetting industry. Lorem Ipsum has been the industry's standard dummy text ever since the 1500s, when an unknown printer took a galley of type and scrambled it to make a type specimen typesetting industry. Lorem Ipsum has been the industry's standard dummy text ever since the 1500s, when an unknown printer took a galley of type and scrambled it to make a type specimen not only five centuries.</p>
</div>
<div class="abs btn-dark">Read More</div>

<div class="abs thumbs"></div>
<svg class="abs mini" style="left:119px" viewBox="0 0 18 18"><circle cx="9" cy="9" r="8" fill="#eee" stroke="#999"/><path d="M6 9 L11 6 L11 12Z" fill="#333"/></svg>
<svg class="abs mini" style="left:819px" viewBox="0 0 18 18"><circle cx="9" cy="9" r="8" fill="#eee" stroke="#999"/><path d="M12 9 L7 6 L7 12Z" fill="#333"/></svg>
<div class="abs thumb t1" role="img" aria-label="Striped tablecloth with glass vase"></div>
<div class="abs thumb t2" role="img" aria-label="Linen on driftwood at the beach"></div>
<div class="abs thumb t3" role="img" aria-label="Colourful patterned fabrics and curtains"></div>
<div class="abs thumb t4" role="img" aria-label="Wooden blinds in a living room"></div>
<div class="abs thumb t5" role="img" aria-label="Wall of fabric rolls in the shop"></div>

<div class="abs lower"></div>
<svg class="abs col-icon" style="left:101px" width="28" height="24" viewBox="0 0 28 24"><g transform="rotate(-12 14 12)"><rect x="3" y="4" width="22" height="16" rx="1" fill="#f3f1e6" stroke="var(--icon)"/><rect x="6" y="7" width="7" height="5" fill="#c9c6b8"/><path d="M15 8h7M15 11h7M6 15h16M6 17.5h16" stroke="var(--icon)" stroke-width="1"/></g></svg>
<div class="abs col-title" style="left:139px">Lastest News</div>
<div class="abs col-rule" style="left:99px;width:238px"></div>
<div class="abs news-arrow" style="top:980px">➜</div>
<div class="abs news-item" style="top:976px">Mobile Marketing: Too Big an Opportunity for Companies to Ignore</div>
<div class="abs posted" style="top:1010px">Posted on: Monday, November 12, 2012</div>
<div class="abs news-arrow" style="top:1035px">➜</div>
<div class="abs news-item" style="top:1031px">Mobile Marketing: Too Big an Opportunity for Companies to Ignore</div>
<div class="abs posted" style="top:1065px">Posted on: Monday, November 12, 2012</div>
<div class="abs view-all">View all</div>

<svg class="abs col-icon" style="left:358px" width="26" height="22" viewBox="0 0 26 22"><path d="M3 2h20a2 2 0 0 1 2 2v10a2 2 0 0 1-2 2H11l-5 5v-5H3a2 2 0 0 1-2-2V4a2 2 0 0 1 2-2z" fill="#e8e8e8" stroke="var(--icon)"/><path d="M8 6h3v3l-2 3h-1l1-3H8zM14 6h3v3l-2 3h-1l1-3h-1z" fill="#666"/></svg>
<div class="abs col-title" style="left:392px">Customer Testimonals</div>
<div class="abs col-rule" style="left:359px;width:238px"></div>
<div class="abs video" role="img" aria-label="Video still of rolls of patterned fabric in the shop"></div>
<svg class="abs" style="left:456px;top:1030px" width="40" height="30" viewBox="0 0 40 30"><rect width="40" height="30" rx="4" fill="rgba(0,0,0,.55)"/><path d="M15 8 L27 15 L15 22Z" fill="#fff"/></svg>

<svg class="abs col-icon" style="left:617px" width="26" height="20" viewBox="0 0 26 20"><rect x="1" y="2" width="24" height="16" rx="1" fill="#f2f2f2" stroke="var(--icon)"/><path d="M1 2 L13 11 L25 2M1 18 L10 9M25 18 L16 9" fill="none" stroke="var(--icon)"/></svg>
<div class="abs col-title" style="left:650px">Newsletter Subscribe</div>
<div class="abs col-rule" style="left:618px;width:238px"></div>
<div class="abs input" style="top:982px">Enter your Name</div>
<div class="abs input" style="top:1021px">Enter your Email</div>
<div class="abs submit">SUBMIT</div>

<div class="abs footer"></div>
<div class="abs footer-links">Fashion fabrics &nbsp;|&nbsp; Table linen &nbsp;|&nbsp; Decorative fabrics &nbsp;|&nbsp; Retrieval Systems &nbsp;|&nbsp; Scholarships &nbsp;|&nbsp; Contact &nbsp;|&nbsp; Stock sale</div>
<div class="abs copyright">Copyright © 2012 velunor.co.au. All rights reserved.</div>
<div class="abs bottom-rule"></div>
</body>
</html>
```